Graphic lion print design with text

I like the gold effects in image 2 as described in my attached document, but i'm open to other suggestions. The desired image is image 1. This is a gift for a Leo friend. This is going to be printed and framed to be hung on the wall in a large frame, in landscape format. I like the idea of using different font styles to separate the statements.

• I’m open to the suggestions about the font styles, but I want to separate the statements by using different font styles as shown in attached document.
Must be landscape format.
Small fonts preferred, as shown in the attached image.
• I like the gold effect in image 2 but other suggestions/colours welcome
• Please don't stretch the picture so I can have a good resolution. Place the text on another black background template and then paste the picture beside to the text.

```html
<!DOCTYPE html>
<html lang="en">
<head>
<meta charset="utf-8">
<title>Lion Print – More Than a Conqueror</title>
<link rel="stylesheet" href="https://fonts.googleapis.com/css2?family=Almendra&family=Montserrat:wght@600;700&family=Pinyon+Script&family=Lobster&family=Lobster+Two:ital,wght@1,400;1,700&family=Ubuntu:ital,wght@1,500&family=Playfair+Display:ital@1&family=Cormorant+Garamond:ital,wght@1,500&family=Ultra&family=Grenze+Gotisch:wght@500&family=Kaushan+Script&family=Great+Vibes&family=Cormorant+Upright:wght@500&display=swap">
<style>
  :root {
    --ink: #000;
    --gold: #7e603b;
    --gold-light: #c8904e;
    --gold-deep: #3a2410;
  }
  * { margin: 0; padding: 0; box-sizing: border-box; }
  html, body { width: 1200px; height: 806px; overflow: hidden; background: var(--ink); }
  .canvas { position: relative; width: 1200px; height: 806px; background: var(--ink); color: var(--gold); }
  .line { position: absolute; white-space: nowrap; line-height: 1; }

  .lion-art {
    position: absolute; left: 700px; top: 0; width: 500px; height: 806px;
    background:
      radial-gradient(ellipse 55% 45% at 70% 45%, var(--gold-light) 0%, #8a5c2c 40%, var(--gold-deep) 70%, transparent 90%),
      var(--ink);
  }

  .intro { left: 25px; top: 34px; font-family: "Almendra", serif; font-size: 33px; letter-spacing: 1px; word-spacing: 7px; }
  .headline { left: 0; width: 784px; text-align: center; font-family: "Montserrat", sans-serif; }
  .headline--main { top: 76px; font-size: 25px; font-weight: 700; }
  .headline--sub { top: 106px; font-size: 21px; font-weight: 600; }

  .frame { position: absolute; left: 0; top: 0; }

  .bullet { position: absolute; left: 121px; width: 14px; height: 10px; border: 2px solid var(--gold); border-radius: 50%; }

  .almighty { left: 166px; top: 172px; font-family: "Pinyon Script", cursive; font-size: 44px; }
  .come-through { left: 167px; top: 224px; font-family: "Lobster", cursive; font-size: 28px; }
  .seek { left: 166px; top: 256px; font-family: "Lobster Two", cursive; font-style: italic; font-size: 29px; }
  .him { left: 167px; top: 296px; font-family: "Lobster", cursive; font-size: 38px; }
  .him small { font-family: "Ubuntu", sans-serif; font-style: italic; font-weight: 500; font-size: 21px; margin-left: 4px; }

  .may-god { left: 166px; top: 366px; font-family: "Lobster", cursive; font-size: 28px; }
  .calm { left: 166px; top: 401px; font-family: "Playfair Display", serif; font-style: italic; font-size: 24px; letter-spacing: 2px; word-spacing: 5px; }
  .and { left: 168px; top: 424px; font-family: "Pinyon Script", cursive; font-size: 40px; }
  .still { left: 167px; top: 468px; font-family: "Cormorant Garamond", serif; font-style: italic; font-weight: 500; font-size: 25px; letter-spacing: 2px; }

  .doors { left: 167px; top: 521px; font-family: "Cormorant Upright", serif; font-weight: 500; font-size: 30px; }
  .doors strong { font-family: "Ultra", serif; font-weight: 400; font-size: 27px; margin-right: 8px; }
  .places { left: 168px; top: 561px; font-family: "Grenze Gotisch", serif; font-weight: 500; font-size: 29px; letter-spacing: 1px; word-spacing: 5px; }

  .waters { left: 46px; top: 648px; font-family: "Kaushan Script", cursive; font-size: 28px; }
  .never { left: 72px; top: 684px; font-family: "Great Vibes", cursive; font-size: 37px; }
  .amen { left: 0; width: 784px; top: 730px; text-align: center; font-family: "Grenze Gotisch", serif; font-size: 40px; }
</style>
</head>
<body>
<main class="canvas">
  <div class="lion-art" role="img" aria-label="Gold-toned roaring lion head in profile with glowing dust particles on black"></div>

  <p class="line intro">It doesn’t matter who or what may come against you,</p>
  <p class="line headline headline--main">FOR GOD IS WITH YOU</p>
  <p class="line headline headline--sub">HE has made you more than a conqueror.</p>

  <svg class="frame" width="720" height="640" viewBox="0 0 720 640" aria-hidden="true">
    <g stroke="var(--gold)" stroke-width="1" fill="none">
      <line x1="105" y1="154" x2="677" y2="154"/>
      <line x1="105" y1="619" x2="677" y2="619"/>
      <line x1="95" y1="156" x2="95" y2="617"/>
      <line x1="685" y1="156" x2="685" y2="617"/>
      <path d="M260 154 Q380 140 500 154" stroke-width="3"/>
      <path d="M260 619 Q380 605 500 619" stroke-width="3"/>
    </g>
  </svg>

  <span class="bullet" style="top:191px"></span>
  <span class="bullet" style="top:378px"></span>
  <span class="bullet" style="top:534px"></span>

  <p class="line almighty">Almighty God</p>
  <p class="line come-through">will come through for you</p>
  <p class="line seek">when you seek</p>
  <p class="line him">Him<small>in your moments of trouble and unrest.</small></p>

  <p class="line may-god">May God</p>
  <p class="line calm">calm the restlessness of your mind</p>
  <p class="line and">And</p>
  <p class="line still">still the thoughts that worry you.</p>

  <p class="line doors"><strong>DOORS</strong>will open for you,</p>
  <p class="line places">in the most unlikeliest of places.</p>

  <p class="line waters">When you go through deep waters&nbsp; He will be with you</p>
  <p class="line never">Never will He leave you, Never will He forsake you.</p>
  <p class="line amen">Amen.</p>
</main>
</body>
</html>
```